Modern Business Card that captures our business as a whole

Hi! We'd like our business cards designed to match the materials you've made for us previously. We'd like a contemporary design. No need to have any person's names on the card, as we'd like to be able to use them generically for all providers. (Not sure how that is typically done) I've included information about our practice attached. The name logo, practice locations, maybe basic info about us

Industry/Entity Type

mental healthcare

Contact Information for Business Card

Requirements
Must have
• QR code, locations, web address, 1800 number, captures who we are and what we do.
Should not have
• individual doctors' names

```html
<!DOCTYPE html>
<html lang="en">
<head>
<meta charset="utf-8">
<title>Harborlight Wellness Group – Business Card</title>
<link rel="stylesheet" href="https://fonts.googleapis.com/css2?family=Oswald:wght@500&family=Questrial&display=swap">
<style>
  :root {
    --bg: #1f1f1f;
    --olive: #a9a56c;
    --ink: #2a2a2a;
    --paper: #ffffff;
    --card-dark: #141414;
  }
  * { margin: 0; padding: 0; box-sizing: border-box; }
  html, body { width: 1200px; height: 801px; overflow: hidden; }
  body {
    background: var(--bg);
    font-family: "Questrial", sans-serif;
    display: flex;
    align-items: center;
    justify-content: center;
    gap: 40px;
  }
  .card {
    width: 540px;
    height: 309px;
    position: relative;
    border: 3px solid var(--olive);
  }
  /* Front: contact side */
  .card-front {
    background: var(--paper);
    color: var(--ink);
    padding: 30px 30px 26px 34px;
    display: flex;
    flex-direction: column;
    justify-content: space-between;
  }
  .front-top {
    display: flex;
    align-items: center;
    gap: 22px;
  }
  .brand-name {
    font-family: "Oswald", sans-serif;
    font-weight: 500;
    color: var(--olive);
    text-transform: uppercase;
    letter-spacing: 0.5px;
    line-height: 1.15;
  }
  .card-front .brand-name { font-size: 19px; width: 150px; }
  .divider {
    width: 1px;
    height: 70px;
    background: var(--olive);
  }
  .contact-list { list-style: none; font-size: 14px; line-height: 1.65; }
  .contact-list li { display: flex; align-items: center; gap: 8px; }
  .contact-list svg { width: 11px; height: 11px; fill: var(--ink); flex: none; }
  .locations {
    display: grid;
    grid-template-columns: 1fr 1fr 1.15fr;
    gap: 18px;
    font-size: 11.5px;
    line-height: 1.4;
  }
  .location + .location { margin-top: 8px; }
  .location-name { color: var(--olive); }
  /* Back: brand side */
  .card-back {
    background: linear-gradient(135deg, #1b1b1b 0%, var(--card-dark) 60%, #101010 100%);
    display: flex;
    align-items: center;
    justify-content: center;
  }
  .card-back .brand-name {
    font-size: 30px;
    letter-spacing: 1px;
  }
</style>
</head>
<body>
  <section class="card card-front" aria-label="Business card, contact side">
    <div class="front-top">
      <p class="brand-name">Harborlight Wellness Group</p>
      <span class="divider"></span>
      <ul class="contact-list">
        <li><svg viewBox="0 0 24 24"><path d="M6.6 10.8a15.2 15.2 0 0 0 6.6 6.6l2.2-2.2a1 1 0 0 1 1-.25 11.4 11.4 0 0 0 3.6.57 1 1 0 0 1 1 1V20a1 1 0 0 1-1 1A17 17 0 0 1 3 4a1 1 0 0 1 1-1h3.5a1 1 0 0 1 1 1c0 1.25.2 2.45.57 3.57a1 1 0 0 1-.25 1z"/></svg>(800) 555-0142</li>
        <li><svg viewBox="0 0 24 24"><path d="M2 5h20v14H2zm2 2v.5l8 5 8-5V7z"/></svg>info@HarborlightWellness.com</li>
        <li><svg viewBox="0 0 24 24"><circle cx="12" cy="12" r="10"/></svg>HarborlightWellness.com</li>
      </ul>
    </div>
    <div class="locations">
      <div>
        <p class="location"><span class="location-name">HWG Linden Park</span><br>2240 Maple Ave, Ste 4,<br>Linden Park NJ 08120</p>
        <p class="location"><span class="location-name">HWG FamilyCare</span><br>2260 Maple Ave, Ste B12,<br>Linden Park NJ 08120</p>
      </div>
      <div>
        <p class="location"><span class="location-name">HWG Westbrook</span><br>418 Alder St, Ste C2,<br>Westbrook, NJ 08650</p>
        <p class="location"><span class="location-name">HWG Fairmont</span><br>905 Orchard Rd, Ste 310,<br>Fairmont, PA 19120</p>
      </div>
      <div>
        <p class="location"><span class="location-name">HWG Central Valley</span><br>75 W. Birch St., 2nd floor,<br>Milford, NY 13200</p>
      </div>
    </div>
  </section>

  <section class="card card-back" aria-label="Business card, brand side">
    <p class="brand-name">Harborlight Wellness Group</p>
  </section>
</body>
</html>
```